Bramwell Dental personal information forms

We are a Dental Practice that require an update to our information forms, there are 3 versions of it.
I will attach our old ones, we need to keep the same information on there, we just want them to look better and use our current logo and colours.
Our website is www.bramwelldental-example.net
Our facebook is www.facebook.com/bramwelldentalkestonwalk/
..................................................................................................

Target Market(s)

Everyone, easy to read

Industry/Entity Type

Dental Clinic

Colors
0692cd
34a6d7
cee9f5
ffffff
0255a3
3276b5

Requirements
Must have
• Logo
• Our colours
• same information as the uploaded versions
Should not have
• any other colour besides the blues, black and white

```html
<!DOCTYPE html>
<html lang="en">
<head>
<meta charset="utf-8">
<title>Bramwell Dental – Patient Information Form</title>
<link href="https://fonts.googleapis.com/css2?family=Open+Sans:ital,wght@0,400;0,600;0,700;1,600;1,700&display=swap" rel="stylesheet">
<style>
:root{
  --bar:#3276b5;
  --navy:#0255a3;
  --brand:#0692cd;
  --sky:#34a6d7;
  --pale:#cee9f5;
  --field:#dbe2f3;
  --ink:#231f20;
  --backdrop:#939598;
  --white:#ffffff;
}
*{box-sizing:border-box;margin:0;padding:0}
html,body{width:1200px;height:792px;overflow:hidden;background:var(--backdrop)}
body{font-family:"Open Sans",Arial,sans-serif;color:var(--ink)}
.stage{position:relative;width:1353px;height:892px;transform:scale(0.88692);transform-origin:0 0}
.page{position:absolute;top:50px;width:612px;height:792px;background:var(--white)}
.page--one{left:48px}
.page--two{left:686px}
.abs{position:absolute}

.header-band{position:absolute;left:0;top:0;width:612px;height:128px;background:linear-gradient(180deg,#e4ecf6 0%,#f3f6fb 60%,#ffffff 100%)}
.header-rule{position:absolute;left:0;top:0;width:612px;height:6px;background:var(--bar)}
.logo-block{position:absolute;left:170px;top:6px;width:272px;height:44px;background:var(--bar);clip-path:polygon(0 0,100% 0,92% 100%,8% 100%);display:flex;align-items:center;justify-content:center}
.logo-name{color:var(--white);font-weight:600;font-size:22px;letter-spacing:.5px}
.practitioners{left:42px;top:86px;font-size:10.5px;line-height:13px}
.welcome{left:376px;top:91px;font-size:13.5px;font-weight:700;font-style:italic}
.intro{left:32px;top:129px;width:550px;font-size:10.2px;line-height:14px;text-align:justify}

.frame{position:absolute;border:1px solid var(--bar)}
.bar{position:absolute;height:14px;background:var(--bar);color:var(--white);font-size:10px;line-height:14px;text-align:center}

table.grid{position:absolute;border-collapse:collapse;table-layout:fixed;font-size:10px}
table.grid td{border:1px solid var(--bar);height:15px;padding:0 5px;line-height:13px;vertical-align:top;white-space:nowrap}
table.grid td.head{background:var(--bar);color:var(--white);text-align:center}
table.grid td.right{text-align:right}

.cb{display:inline-block;width:7px;height:7px;border:1px solid var(--ink);margin-right:4px;vertical-align:0}
.row{display:flex;align-items:center;font-size:10px}
.q{font-size:8.4px;font-weight:600}
.yesno{position:absolute;right:40px;font-size:8px;font-weight:600;display:flex;gap:8px}
.options{display:flex;font-size:8px}
.box{position:absolute;border:1px solid var(--bar)}
.note{left:44px;top:634px;width:534px;font-size:8.3px;font-weight:700;font-style:italic;line-height:13px}
.page-turn{right:32px;top:746px;font-size:8px;font-weight:600}
.url{position:absolute;left:0;width:612px;top:772px;text-align:center;font-size:9.5px;letter-spacing:3.2px}

.p2-text{font-size:10px;line-height:14px}
.section-title{color:var(--brand);font-weight:700;font-size:10px}
.check-grid{position:absolute;display:grid;grid-auto-flow:column;font-size:7.8px;line-height:12px}
.check-grid .item{display:flex;align-items:flex-start}
.check-grid .cb{margin-top:2px;margin-right:6px}
.field{position:absolute;left:42px;width:530px;height:14px;background:var(--field)}
.declaration{left:42px;top:661px;width:532px;font-size:8.4px;font-weight:700;font-style:italic;line-height:12px}
.small-print{left:42px;top:685px;width:532px;font-size:7.2px;line-height:10px}
.signature{left:46px;top:740px;font-size:8.4px;font-weight:600;display:flex;align-items:flex-end}
.signature .line{display:inline-block;border-bottom:1px solid var(--bar);height:1px;margin:0 16px 0 4px}
</style>
</head>
<body>
<div class="stage">

  <section class="page page--one">
    <div class="header-band" role="img" aria-label="Soft photograph of dental instruments and a tooth model"></div>
    <div class="header-rule"></div>
    <div class="logo-block"><span class="logo-name">Bramwell Dental</span></div>
    <p class="abs practitioners">Dr. Colin Hartwell &amp; Dr. Simon Ashby<br>Dental Surgeons</p>
    <p class="abs welcome">Welcome back to our practive!</p>
    <p class="abs intro">THIS INFORMATION IS CONFIDENTIAL and is necessary to enable us to offer you THE BEST POSSIBLE CARE. At Bramwell Dental, we respect and protect the privacy of our patients and as such will only ask for information relevant to the treatment we may need to provide you. Thank you!</p>

    <div class="frame" style="left:32px;top:180px;width:550px;height:583px"></div>
    <div class="bar" style="left:32px;top:180px;width:550px"></div>
    <div class="abs" style="left:32px;top:180px;width:270px;color:#fff;font-size:10px;line-height:14px;text-align:center">PATIENT INFORMATION</div>
    <div class="abs" style="left:364px;top:180px;width:208px;color:#fff;font-size:10px;line-height:14px;text-align:center">PATIENT CONTACT INFORMATION</div>

    <div class="abs row" style="left:46px;top:197px;gap:8px">
      <span><span class="cb"></span>Ms</span><span><span class="cb"></span>Mrs</span><span><span class="cb"></span>Miss</span><span><span class="cb"></span>Mr</span><span><span class="cb"></span>Master</span><span><span class="cb"></span>Dr</span><span><span class="cb"></span>Other</span>
    </div>

    <table class="grid patient-details" style="left:44px;top:215px;width:290px">
      <colgroup><col style="width:89px"><col style="width:110px"><col></colgroup>
      <tr><td>Surname</td><td colspan="2"></td></tr>
      <tr><td>First Name</td><td colspan="2"></td></tr>
      <tr><td>Prefered</td><td colspan="2"></td></tr>
      <tr><td>Date of Birth</td><td colspan="2"></td></tr>
      <tr><td rowspan="3" style="line-height:15px">Current<br>Residential<br>Address</td><td colspan="2"></td></tr>
      <tr><td colspan="2"></td></tr>
      <tr><td></td><td>Postcode:</td></tr>
      <tr><td rowspan="4" style="line-height:15px">Postal<br>Residential<br>Address<br>(if different)</td><td colspan="2"></td></tr>
      <tr><td colspan="2"></td></tr>
      <tr><td colspan="2"></td></tr>
      <tr><td></td><td>Postcode:</td></tr>
      <tr><td>Occupation</td><td colspan="2"></td></tr>
      <tr><td>Employer</td><td colspan="2"></td></tr>
    </table>

    <table class="grid contact-details" style="left:364px;top:215px;width:208px">
      <colgroup><col style="width:62px"><col></colgroup>
      <tr><td>Phone</td><td>M:</td></tr>
      <tr><td></td><td>H:</td></tr>
      <tr><td></td><td>W:</td></tr>
      <tr><td>Email</td><td></td></tr>
      <tr><td>Prefered</td><td></td></tr>
      <tr><td colspan="2">Prefered Method of communication</td></tr>
      <tr><td colspan="2"><span class="cb"></span>SMS &nbsp;<span class="cb"></span>Phone &nbsp;<span class="cb"></span>Email &nbsp;<span class="cb"></span>Mail</td></tr>
    </table>

    <table class="grid emergency-contact" style="left:364px;top:330px;width:208px">
      <colgroup><col style="width:62px"><col></colgroup>
      <tr><td colspan="2" class="head">EMERGENCY CONTACT</td></tr>
      <tr><td>Name</td><td></td></tr>
      <tr><td>Relation</td><td></td></tr>
      <tr><td style="height:30px;line-height:15px">Contact<br>Number</td><td></td></tr>
    </table>

    <div class="bar" style="left:32px;top:418px;width:550px">OTHER INFORMATION</div>

    <table class="grid account-holder" style="left:44px;top:441px;width:528px">
      <colgroup><col style="width:62px"><col style="width:216px"><col style="width:94px"><col></colgroup>
      <tr><td colspan="4" class="head">Person responsible for your account (inyourself, please tick this box <span class="cb" style="border-color:#fff;background:#fff"></span>)</td></tr>
      <tr><td>Name</td><td></td><td colspan="2">Relationship</td></tr>
      <tr><td>Phone</td><td colspan="3"></td></tr>
      <tr><td rowspan="2">Address</td><td colspan="3"></td></tr>
      <tr><td colspan="2"></td><td>Postcode</td></tr>
    </table>

    <p class="abs q" style="left:44px;top:527px">Do you have Private Health Insurance? If YES, please specify the name (e.g. MEDCOVER)</p>
    <div class="yesno" style="top:527px"><span><span class="cb"></span>YES</span><span><span class="cb"></span>NO</span></div>
    <table class="grid insurance" style="left:44px;top:543px;width:528px;font-size:9.5px">
      <colgroup><col style="width:52px"><col></colgroup>
      <tr><td>Name</td><td></td></tr>
      <tr><td>Phone</td><td></td></tr>
    </table>

    <p class="abs q" style="left:44px;top:578px">Are you claiming for your tretament under a Goverment Dental Benefits Scheme?</p>
    <div class="yesno" style="top:578px"><span><span class="cb"></span>YES</span><span><span class="cb"></span>NO</span></div>
    <div class="box" style="left:44px;top:593px;width:528px;height:30px;padding:3px 6px">
      <p class="q">If YES, please tick one of the following option:</p>
      <div class="options" style="margin-top:2px">
        <span style="width:62px"><span class="cb"></span>CDSS</span><span style="width:60px"><span class="cb"></span>DVD</span><span style="width:102px"><span class="cb"></span>Carecomp</span><span style="width:72px"><span class="cb"></span>MVC</span><span><span class="cb"></span>Other:</span>
      </div>
    </div>

    <p class="abs note">Please note: if your are claiming please ensure that you have the relevant letters and/or forms as payment is required at time to treatment</p>

    <div class="box" style="left:44px;top:665px;width:528px;height:30px;padding:3px 6px">
      <p class="q">How did you hear about us? (please circle one option below)</p>
      <div class="options" style="margin-top:2px">
        <span style="width:62px"><span class="cb"></span>Referred</span><span style="width:82px"><span class="cb"></span>Town pages</span><span style="width:108px"><span class="cb"></span>Advertisement</span><span style="width:64px"><span class="cb"></span>Internet</span><span><span class="cb"></span>Other:</span>
      </div>
    </div>

    <table class="grid referrer" style="left:44px;top:699px;width:528px;font-size:8.4px;font-weight:600">
      <colgroup><col style="width:190px"><col></colgroup>
      <tr><td>If reffered please provide name of referrer:</td><td></td></tr>
      <tr><td>Relationship to you:</td><td></td></tr>
    </table>

    <p class="abs page-turn">Page 1 of 2, please turn over</p>
    <p class="url">www.bramwelldental-example.net</p>
  </section>

  <section class="page page--two">
    <div class="frame" style="left:34px;top:22px;width:548px;height:740px"></div>
    <p class="abs p2-text" style="left:46px;top:33px;width:528px">it is essential that we know about your past and present medical history. Many medical conditions my interfere with dental procedures. please take you time and thoroughly complete the following session.</p>

    <p class="abs section-title" style="left:46px;top:66px">DENTAL HISTORY</p>
    <p class="abs p2-text" style="left:46px;top:79px">Are you concerned about or expeiencing any of the following dental problem? (please tick as many as applies)</p>
    <div class="check-grid" style="left:54px;top:97px;grid-template-rows:repeat(4,12px);grid-template-columns:136px 170px 200px">
      <span class="item"><span class="cb"></span>Sensitive to hot or cold</span>
      <span class="item"><span class="cb"></span>Stining of your teeth</span>
      <span class="item"><span class="cb"></span>Bleeding Gums</span>
      <span class="item"><span class="cb"></span>Crowding of teeth</span>
      <span class="item"><span class="cb"></span>Food trapping between teeth</span>
      <span class="item"><span class="cb"></span>Discoloured Fillings</span>
      <span class="item"><span class="cb"></span>Bad breath</span>
      <span class="item" style="line-height:10px"><span class="cb"></span>Grinding/ Clenching of<br>your teeth</span>
      <span class="item"><span class="cb"></span>Clicking/pain in the jaw joints</span>
      <span class="item"><span class="cb"></span>Roughness of existing fillings</span>
      <span class="item"><span class="cb"></span>Tenderness when eating</span>
      <span class="item"><span class="cb"></span>Poorly fitted crowns/dentures.</span>
    </div>

    <p class="abs q" style="left:46px;top:161px">What is the main purpose of your visit today?</p>
    <div class="field" style="top:174px"></div>
    <p class="abs q" style="left:46px;top:194px">How long has it been since yout last dental visit?</p>
    <div class="field" style="top:207px"></div>
    <p class="abs q" style="left:46px;top:225px">Does dental treatment make you nervous?</p>
    <div class="abs options" style="left:54px;top:238px;font-weight:600">
      <span style="width:66px"><span class="cb"></span>No</span><span style="width:82px"><span class="cb"></span>Slightly</span><span style="width:104px"><span class="cb"></span>Moderately</span><span><span class="cb"></span>Extreemly</span>
    </div>

    <table class="grid medical-contacts" style="left:44px;top:257px;width:528px">
      <colgroup><col style="width:174px"><col></colgroup>
      <tr><td colspan="2" class="head" style="text-align:left">MEDICAL HISTORY</td></tr>
      <tr><td>Name of your family Doctor (GP)</td><td></td></tr>
      <tr><td class="right">Clinic</td><td></td></tr>
      <tr><td class="right">Phone</td><td></td></tr>
    </table>

    <p class="abs q" style="left:46px;top:329px;line-height:12px">Are you currently or have you taken any prescribed medication or dietary supplements in the last 12 months?<br>(If YES, Please list below)</p>
    <div class="yesno" style="top:329px"><span><span class="cb"></span>YES</span><span><span class="cb"></span>NO</span></div>
    <div class="field" style="top:356px"></div>

    <p class="abs q" style="left:46px;top:376px">Allegies / Reactions? (If YES, Please list below)</p>
    <div class="yesno" style="top:376px"><span><span class="cb"></span>YES</span><span><span class="cb"></span>NO</span></div>
    <div class="field" style="top:389px"></div>

    <p class="abs q" style="left:46px;top:413px">Have you ever has or are your suffering from any of the following? please tick any that apply:</p>
    <div class="check-grid" style="left:64px;top:434px;grid-template-rows:repeat(8,12px);grid-template-columns:154px 154px 160px">
      <span class="item"><span class="cb"></span>Rheumatic fever</span>
      <span class="item"><span class="cb"></span>Epilepsy</span>
      <span class="item"><span class="cb"></span>Asthma</span>
      <span class="item"><span class="cb"></span>Tuberculosis</span>
      <span class="item"><span class="cb"></span>Radiation Therapy</span>
      <span class="item"><span class="cb"></span>Sizziness, fainting</span>
      <span class="item"><span class="cb"></span>Hepatitis A B or C</span>
      <span class="item"><span class="cb"></span>Recent eye surgery</span>
      <span class="item"><span class="cb"></span>Diabetes</span>
      <span class="item"><span class="cb"></span>Kidney Disease</span>
      <span class="item"><span class="cb"></span>Heart Attack</span>
      <span class="item"><span class="cb"></span>High Blood Pressure</span>
      <span class="item"><span class="cb"></span>Bleeding problems</span>
      <span class="item"><span class="cb"></span>Artificial joints</span>
      <span class="item"><span class="cb"></span>Respiratory problems</span>
      <span class="item"></span>
      <span class="item"><span class="cb"></span>HIVE positive</span>
      <span class="item"><span class="cb"></span>High cholesterol</span>
      <span class="item"><span class="cb"></span>Cancer</span>
      <span class="item"><span class="cb"></span>Pace-maker</span>
      <span class="item"><span class="cb"></span>Osteoporosis</span>
      <span class="item"><span class="cb"></span>Heat rate problems</span>
      <span class="item"><span class="cb"></span>Heart murmur</span>
    </div>

    <p class="abs q" style="left:46px;top:556px">Do you have any disease, or condition or problem not listed above?</p>
    <div class="yesno" style="top:556px"><span><span class="cb"></span>YES</span><span><span class="cb"></span>NO</span></div>
    <div class="field" style="top:570px"></div>

    <p class="abs q" style="left:46px;top:591px">Have you had surgery or been to hospital in the last 5 years? |(if YES, please give details)</p>
    <div class="yesno" style="top:591px"><span><span class="cb"></span>YES</span><span><span class="cb"></span>NO</span></div>
    <div class="field" style="top:604px"></div>

    <p class="abs q" style="left:46px;top:625px">For Women: Are you pregnant? If YES, how many months?</p>
    <div class="yesno" style="top:625px"><span><span class="cb"></span>YES</span><span><span class="cb"></span>NO</span></div>
    <div class="field" style="top:638px"></div>

    <p class="abs declaration">The information that I provided is to the best of my knowledge tru and current and I understand that it is my responsibility to inform of any changes in my medical status.</p>
    <p class="abs small-print">This is to certify that I, the undersigned, consent to the performing of the dental and oral surgery procedure agreed to be necessary or advisable, include the use of local anaesthetic as indicated and I will assume responsibility&nbsp; for the fees associated with these procedures. Therefore, I shall pay any legal cost, including solicitor own costs, tracing costs and may collection commission incurred by Bramwell Dental as a result of my failure to pay any amount due to Bramwell Dental.</p>

    <div class="abs signature">
      <span>Patient/Parent/Person Responsible Signature:</span><span class="line" style="width:148px"></span>
      <span>Date:</span><span class="line" style="width:146px;margin-right:0"></span>
    </div>

    <p class="url">www.bramwelldental-example.net</p>
  </section>

</div>
</body>
</html>
```